"Cork Hollow Excursions" is a top notch Sable Ridge Valley Wine Tour company.

We provide scenic, boutique and custom wine tours. I need the card to be clean and classy. I will provide our logo. I would like the logo to cover the back side of the card as an option and would like to see a couple color options other then our signature green and gold. I would like to see some creative options and let the designers come up with options.
I need cards for myself and my team. The final design should communicate "An authentic and boutique wine tour experience"
Please use my website for reference www.corkhollowexcursions.com

Target Market(s)

We have a wide range of clients from millennials to baby boomers

Industry/Entity Type

Tour

Contact Information for Business Card

Contact info:
Dale Munford
805-291-6384
info@corkhollowexcursions.com
corkhollowexcursions.com

Colors

Designer to choose colors to be used in the design.

Requirements
Must have
• my logo
Nice to have
• *I would like to have the backside side with the logo and the company statement
• "An authentic and boutique wine tour experience" as an option.
• *I would also like to see what the designers can create!
• *I would like to see an option that incorporates or social: snapgrid, rovia, route scout
Should not have
• I do not want it too busy.

```html
<!DOCTYPE html>
<html lang="en">
<head>
<meta charset="utf-8">
<title>Cork Hollow Excursions — Business Card</title>
<link rel="stylesheet" href="https://fonts.googleapis.com/css2?family=Cinzel:wght@400;500&family=Open+Sans:wght@400;600&display=swap">
<style>
  :root {
    --stage: #9e9e9e;
    --vine-green: #276745;
    --paper: #ffffff;
    --gold: #a8876a;
    --shadow: rgba(0, 0, 0, 0.45);
  }
  * { margin: 0; padding: 0; box-sizing: border-box; }
  html, body {
    width: 1200px;
    height: 900px;
    overflow: hidden;
    background: var(--stage);
  }
  .canvas { position: relative; width: 1200px; height: 900px; }
  .card {
    position: absolute;
    top: 307px;
    width: 440px;
    height: 272px;
    overflow: hidden;
    box-shadow: 3px 4px 6px var(--shadow);
  }

  .wordmark {
    position: absolute;
    font-family: "Cinzel", serif;
    font-weight: 500;
    line-height: 1;
    text-align: center;
  }
  .wordmark .wordmark-main { display: block; white-space: nowrap; }
  .wordmark .wordmark-sub {
    display: flex;
    align-items: center;
    gap: 6px;
    letter-spacing: 2px;
  }
  .wordmark .wordmark-sub::before,
  .wordmark .wordmark-sub::after {
    content: "";
    flex: 1;
    height: 1px;
    background: currentColor;
  }

  /* Front */
  .card-front {
    left: 150px;
    background: var(--vine-green);
    border-radius: 3px 3px 10px 10px;
    color: var(--paper);
  }
  .front-wordmark {
    left: 22px;
    top: 36px;
    width: 282px;
    color: var(--paper);
  }
  .front-wordmark .wordmark-main { font-size: 35px; }
  .front-wordmark .wordmark-sub { font-size: 15px; margin: 1px 8px 0 12px; }
  .person-name {
    position: absolute;
    left: 22px;
    top: 114px;
    font-family: "Cinzel", serif;
    font-size: 19px;
    font-weight: 400;
  }
  .contact-list {
    position: absolute;
    left: 22px;
    top: 157px;
    list-style: none;
    font-family: "Open Sans", sans-serif;
    font-size: 12px;
    line-height: 16.5px;
  }
  .contact-list li { display: flex; align-items: center; gap: 5px; }
  .contact-list svg { width: 10px; height: 10px; fill: var(--paper); flex: none; }
  .social-list {
    position: absolute;
    right: 20px;
    top: 168px;
    display: flex;
    gap: 8px;
    list-style: none;
    font-family: "Open Sans", sans-serif;
    font-size: 11px;
    font-weight: 600;
  }
  .social-list li { display: flex; align-items: center; gap: 3px; }
  .social-list .dot { width: 7px; height: 7px; border-radius: 50%; background: var(--paper); }
  .vineyard-band {
    position: absolute;
    left: 0;
    bottom: 0;
    width: 440px;
    height: 58px;
  }

  /* Back */
  .card-back { left: 608px; background: var(--paper); }
  .back-emblem {
    position: absolute;
    left: 147px;
    top: 46px;
    width: 154px;
    height: 88px;
  }
  .back-wordmark {
    left: 84px;
    top: 150px;
    width: 278px;
    color: var(--gold);
  }
  .back-wordmark .wordmark-main { font-size: 34px; }
  .back-wordmark .wordmark-sub { font-size: 17px; margin-top: 0; }
  .back-region {
    position: absolute;
    left: 84px;
    width: 278px;
    top: 200px;
    text-align: center;
    font-family: "Cinzel", serif;
    font-size: 11px;
    letter-spacing: 4.2px;
    color: var(--vine-green);
    white-space: nowrap;
  }
</style>
</head>
<body>
<main class="canvas">

  <section class="card card-front" aria-label="Business card front">
    <h1 class="wordmark front-wordmark">
      <span class="wordmark-main">Cork Hollow</span>
      <span class="wordmark-sub">Excursions</span>
    </h1>

    <p class="person-name">Dale Munford</p>

    <ul class="contact-list">
      <li>
        <svg viewBox="0 0 10 10" aria-hidden="true"><path d="M1 3.5C1 2 2 1 3.5 1h3C8 1 9 2 9 3.5V4H6.8V3H3.2v1H1zM2 5h6l1 4H1z"/></svg>
        805-291-6384
      </li>
      <li>
        <svg viewBox="0 0 10 10" aria-hidden="true"><path d="M0.5 2h9v6h-9z M1 2.4L5 5.6 9 2.4" stroke="#276745" stroke-width="0.8"/></svg>
        info@corkhollowexcursions.com
      </li>
      <li>
        <svg viewBox="0 0 10 10" aria-hidden="true"><circle cx="5" cy="5" r="4.5"/></svg>
        corkhollowexcursions.com
      </li>
    </ul>

    <ul class="social-list" aria-label="Social listings">
      <li><span class="dot"></span>rovia</li>
      <li><span class="dot"></span>route scout</li>
      <li><span class="dot"></span>snapgrid</li>
    </ul>

    <svg class="vineyard-band" viewBox="0 0 440 58" role="img" aria-label="Illustration of vineyard rows rolling across a hillside">
      <defs>
        <linearGradient id="vineyardTone" x1="0" y1="0" x2="0" y2="1">
          <stop offset="0" stop-color="#b9d2c3"/>
          <stop offset="1" stop-color="#e8f0eb"/>
        </linearGradient>
      </defs>
      <path d="M0 16 C90 8 170 6 240 14 C310 22 380 6 440 2 V58 H0 Z" fill="url(#vineyardTone)"/>
    </svg>
  </section>

  <section class="card card-back" aria-label="Business card back">
    <svg class="back-emblem" viewBox="0 0 154 88" role="img" aria-label="Emblem illustration of a rising sun over mountains and vineyard rows">
      <defs>
        <linearGradient id="emblemTone" x1="0" y1="0" x2="0" y2="1">
          <stop offset="0" stop-color="#d6e4db"/>
          <stop offset="1" stop-color="#276745"/>
        </linearGradient>
      </defs>
      <rect width="154" height="88" fill="url(#emblemTone)"/>
    </svg>
    <h2 class="wordmark back-wordmark">
      <span class="wordmark-main">Cork Hollow</span>
      <span class="wordmark-sub">Excursions</span>
    </h2>
    <p class="back-region">Sable Ridge Valley</p>
  </section>

</main>
</body>
</html>
```